Updated web design for software design firm supporting entrepreneurs

Looking for a more modern looking, mobile friendly website design for our company, Plans4Buildables. P4B is a software development firm who supports people who have ideas for software and want to make them a reality. It also provides some maintenance work on existing websites as well as mobile apps. Please see our current website, www.plans4buildables-example.com, for more information on our business.

Old logo files included for reference. However, we are hoping to incorporate a new logo.

Like a blue'ish theme, but open to ideas.

Industry/Entity Type

Software

Logo Text

P4B and/or Plans4Buildables

Number of Pages Required

2 page

Font styles to use
Serif
Sans Serif

Colors
33a6d7
0255a3

Requirements
Must have
• Looking for 2 pages designed: 1 landing page and 1 type of secondary content page
• Please prepare menu for about 7 pages
Nice to have
• This will be implemented as a WordPress theme.
• Could include post-it note, white board, napkins, etc.

```html
<!DOCTYPE html>
<html lang="en">
<head>
<meta charset="utf-8">
<title>Plans4Buildables — Software Development</title>
<link rel="stylesheet" href="https://fonts.googleapis.com/css2?family=Ubuntu:wght@400;500;700&family=Lato:wght@400;700&display=swap">
<style>
:root{
  --navy:#1b2a63;
  --navy-deep:#0f1e5a;
  --navy-bar:#0a1648;
  --link:#3a5bb5;
  --ink:#222;
  --muted:#555;
  --grey-band:#e7e7ed;
  --card-line:#b9b9c2;
  --hero-bg:#2b2b2b;
  --white:#fff;
  --blog-card:#eeeee9;
  --yellow:#f5b92e;
  --teal:#3bb7ac;
  --slate:#4d6497;
}
*{box-sizing:border-box;margin:0;padding:0}
html,body{width:1200px;height:4245px;overflow:hidden}
body{position:relative;font-family:'Lato',Arial,sans-serif;color:var(--ink);background:var(--white);font-size:14px}
.abs{position:absolute}
h2.section-title{font-family:'Ubuntu',Arial,sans-serif;font-weight:500;color:var(--navy);font-size:32px;letter-spacing:.5px;text-transform:uppercase}
.centered{left:0;width:1200px;text-align:center}

/* header */
.site-header{top:0;left:0;width:1200px;height:119px;background:var(--white)}
.brand{left:88px;top:36px;font-family:'Ubuntu',Arial,sans-serif;font-weight:700;font-size:30px;color:var(--navy);display:flex;align-items:center;gap:10px}
.brand i{display:block;width:14px;height:14px;border-radius:50%;background:var(--navy)}
.main-nav{top:48px;left:0;width:1200px}
.main-nav a{position:absolute;font-size:13px;color:var(--ink);text-decoration:none;white-space:nowrap}
.main-nav a.active{color:var(--link)}

/* hero */
.hero{top:119px;left:0;width:1200px;height:413px;background:var(--hero-bg)}
.hero h1{position:absolute;left:88px;top:88px;font-family:'Ubuntu',Arial,sans-serif;font-weight:500;color:var(--white);font-size:36px;line-height:42px}
.hero p{position:absolute;left:88px;top:181px;width:440px;color:var(--white);font-size:14px;line-height:20px}
.hero .btn-outline{position:absolute;left:88px;top:274px;width:178px;height:40px;border:1px solid #ddd;color:var(--white);font-size:11px;display:flex;align-items:center;justify-content:center;letter-spacing:.5px}
.hero .visual{position:absolute;left:594px;top:56px;width:524px;height:306px;background:radial-gradient(circle at 50% 50%,#4a4a48,#2b2b2b 75%)}

/* who we are */
.who .copy{left:88px;width:610px;font-size:13.5px;line-height:20px;color:#333}
.btn-navy{background:var(--navy);color:var(--white);display:flex;align-items:center;justify-content:center;font-size:13px}
.who .photo{left:753px;top:592px;width:351px;height:328px;background:linear-gradient(180deg,#f4f4f4,#dcdcdc);border:1px solid #e0e0e0}

/* services */
.band-grey{left:0;width:1200px;background:var(--grey-band)}
.intro{left:260px;width:680px;text-align:center;font-size:12.5px;line-height:17px;color:#555}
.service-card{top:1220px;width:326px;height:354px;border:1.5px solid var(--card-line);background:#ececf1}
.service-card .icon{position:absolute;left:109px;top:39px;width:108px;height:108px;border-radius:50%;display:flex;align-items:center;justify-content:center}
.service-card h3{position:absolute;top:178px;width:100%;text-align:center;font-family:'Lato',Arial,sans-serif;font-weight:700;font-size:15px;color:#222}
.service-card p{position:absolute;left:55px;top:220px;width:216px;font-size:12.5px;line-height:17px;text-align:justify;color:#333}
.arrow-box{width:34px;height:48px;background:#333;display:flex;align-items:center;justify-content:center}
.arrow-box.light{background:var(--white);border:1px solid #999;width:36px;height:46px}

/* works */
.filters{top:1896px;left:0;width:1200px}
.filters span{position:absolute;height:34px;border:1.5px solid #222;font-size:11.5px;display:flex;align-items:center;justify-content:center;background:var(--white);color:#222}
.filters span.active{background:var(--navy);border-color:var(--navy);color:var(--white)}
.tile{width:334px;height:328px}
.tile.project{background:var(--navy-deep);color:var(--white);padding:110px 32px 0}
.tile.project h4{font-family:'Ubuntu',Arial,sans-serif;font-weight:400;font-size:24px;text-align:center;margin-bottom:18px}
.tile.project p{font-family:'Ubuntu',Arial,sans-serif;font-size:18px;line-height:25px}

/* testimonial */
.quote-text{left:265px;width:670px;font-size:12.5px;line-height:17px;color:#222}

/* blogs */
.blog-card{top:3354px;width:332px;height:368px;background:var(--blog-card)}
.blog-card .thumb{height:243px;border:1px solid #222;border-bottom:5px solid var(--navy-deep)}
.blog-card .tag{position:absolute;left:24px;top:250px;width:40px;height:14px;background:var(--navy-deep);color:var(--white);font-size:8px;display:flex;align-items:center;justify-content:center}
.blog-card h5{position:absolute;left:24px;top:300px;font-size:12.5px;font-weight:700;color:var(--navy)}
.blog-card small{position:absolute;left:24px;top:326px;font-size:9px;color:#333}

/* footer */
.site-footer{top:3976px;left:0;width:1200px;height:213px;background:var(--navy-deep);color:var(--white)}
.site-footer h6{position:absolute;top:52px;font-family:'Ubuntu',Arial,sans-serif;font-weight:400;font-size:20px}
.site-footer .about{position:absolute;left:88px;top:92px;width:215px;font-size:12px;line-height:17px;text-align:justify}
.contact-line{position:absolute;left:467px;display:flex;align-items:center;gap:14px;font-size:12.5px}
.site-footer .sub-copy{position:absolute;left:863px;top:92px;width:250px;font-size:12.5px;line-height:17px}
.sub-field{position:absolute;left:863px;top:146px;width:206px;height:46px;background:#0a1a52;color:#8c96b8;font-size:12px;display:flex;align-items:center;padding-left:22px}
.sub-btn{position:absolute;left:1069px;top:146px;width:44px;height:46px;background:#2e3d73;display:flex;align-items:center;justify-content:center}
.bottom-bar{top:4189px;left:0;width:1200px;height:56px;background:var(--navy-bar);color:var(--white)}
.bottom-bar p{position:absolute;left:88px;top:21px;font-size:11px}
.social{position:absolute;top:16px;width:24px;height:24px;border:1.5px solid var(--white);border-radius:50%}
</style>
</head>
<body>

<header class="site-header abs">
  <div class="brand abs"><i></i>P4B</div>
  <nav class="main-nav abs">
    <a class="active" style="left:636px">Home</a>
    <a style="left:703px">About Us</a>
    <a style="left:796px">Services</a>
    <a style="left:889px">Works</a>
    <a style="left:985px">Blog</a>
    <a style="left:1048px">Contact Us</a>
  </nav>
</header>

<section class="hero abs">
  <h1>TURNING YOUR SOFTWARE<br>VISION INTO REALITY</h1>
  <p>Plans4Buildables can help anyone turn their software idea into reality. We specialize in helping small businesses and individuals take their idea from the back of a napkin to the desktop.</p>
  <div class="btn-outline">PURCHASE NOW</div>
  <div class="visual" role="img" aria-label="Chalkboard sketch of the software development life cycle: requirements, design, implementation, testing and evolution"></div>
</section>

<section class="who">
  <h2 class="section-title abs" style="left:88px;top:588px">Who we are</h2>
  <p class="copy abs" style="top:642px">Plans4Buildables can help anyone turn their software idea into reality. We understand that you don't have to be a big company to have big ideas, but turning those ideas into functional software can be time consuming, expensive and seem out of reach. Plans4Buildables specializes in helping small businesses and individuals take their idea from the back of a napkin to the desktop.</p>
  <p class="copy abs" style="top:738px">As a small business ourselves, we understand the need to be flexible, efficient and cost-conscious. We'll take your idea from a vision in your head to a fully working system.</p>
  <p class="copy abs" style="top:795px">Already have software and need to make improvements? We can help there, too. We've worked with numerous entrepreneurs and companies wanting to update their current software, whether it is making small bug fixes or adding new functionality.</p>
  <div class="btn-navy abs" style="left:85px;top:869px;width:127px;height:37px">View More</div>
  <div class="photo abs" role="img" aria-label="Photo of a smiling support agent wearing a headset"></div>
</section>

<section class="band-grey abs" style="top:990px;height:700px"></section>
<h2 class="section-title abs centered" style="top:1052px">Why take our services</h2>
<p class="intro abs" style="top:1106px">At Plans4Buildables, we love the variety of projects that our clients bring to us and we'd like to share a little bit about the custom work that we've done. However, we take our clients' privacy very seriously, so while you'll be able to get an idea of the kind of work we've done from the below examples, specific references will be provided upon request.</p>

<div class="service-card abs" style="left:99px">
  <div class="icon" style="background:var(--yellow)">
    <svg width="54" height="44" viewBox="0 0 54 44"><rect x="4" y="14" width="32" height="22" rx="3" fill="#222"/><circle cx="13" cy="8" r="6" fill="#222"/><circle cx="27" cy="8" r="6" fill="#222"/><path d="M36 20l14-7v24l-14-7z" fill="#222"/></svg>
  </div>
  <h3>Video Projects</h3>
  <p>Plans4Buildables has built several applications leveraging the use of web-based video. We've done video learning sites that involve</p>
</div>
<div class="service-card abs" style="left:439px">
  <div class="icon" style="background:var(--teal)">
    <svg width="50" height="50" viewBox="0 0 50 50" fill="none" stroke="#fff" stroke-width="3"><circle cx="13" cy="25" r="6"/><circle cx="37" cy="12" r="6"/><circle cx="37" cy="38" r="6"/><path d="M18 22l14-7M18 28l14 7"/></svg>
  </div>
  <h3>Social Networking</h3>
  <p>Plans4Buildables has built several applications leveraging the use of web-based video. We've done video learning sites that involve</p>
</div>
<div class="service-card abs" style="left:775px">
  <div class="icon" style="background:var(--slate)">
    <svg width="30" height="50" viewBox="0 0 30 50"><rect x="2" y="2" width="26" height="46" rx="4" fill="#fff"/><rect x="5" y="8" width="20" height="32" fill="#4fa3e8"/><circle cx="15" cy="44" r="2" fill="#4d6497"/></svg>
  </div>
  <h3>Mobile Apps</h3>
  <p>Plans4Buildables has built several applications leveraging the use of web-based video. We've done video learning sites that involve</p>
</div>
<div class="arrow-box abs" style="left:88px;top:1372px"><svg width="12" height="18"><path d="M10 2L3 9l7 7" stroke="#fff" stroke-width="2" fill="none"/></svg></div>
<div class="arrow-box abs" style="left:1078px;top:1372px"><svg width="12" height="18"><path d="M2 2l7 7-7 7" stroke="#fff" stroke-width="2" fill="none"/></svg></div>

<section class="works">
  <h2 class="section-title abs centered" style="top:1768px">Our works</h2>
  <p class="intro abs" style="top:1822px">At Plans4Buildables, we love the variety of projects that our clients bring to us and we'd like to share a little bit about the custom work that we've done. However, we take our clients' privacy very seriously.</p>
  <div class="filters abs">
    <span class="active" style="left:108px;width:74px">ALL</span>
    <span style="left:195px;width:110px">Video Projects</span>
    <span style="left:311px;width:122px">Social Networking</span>
    <span style="left:441px;width:119px">Mobile Apps</span>
    <span style="left:574px;width:128px">Mapping Software</span>
    <span style="left:710px;width:128px">Online Publishing</span>
    <span style="left:846px;width:128px">API Integration</span>
    <span style="left:982px;width:110px">E-commerce</span>
  </div>
  <div class="tile abs" style="left:85px;top:1967px;background:linear-gradient(135deg,#0e1e3c,#2e5c8a)" role="img" aria-label="Hand touching a glowing video play button"></div>
  <div class="tile project abs" style="left:430px;top:1967px">
    <h4>Project Title</h4>
    <p>We've done video learning sites that involve interactive experiences with a large video</p>
  </div>
  <div class="tile abs" style="left:778px;top:1967px;background:linear-gradient(135deg,#7a2a1a,#3c3f8a)" role="img" aria-label="Hand holding a smartphone showing a mobile app"></div>
  <div class="tile abs" style="left:85px;top:2312px;background:linear-gradient(135deg,#d8d2c8,#7b6a5c)" role="img" aria-label="Person shopping online on a laptop"></div>
  <div class="tile abs" style="left:430px;top:2312px;background:linear-gradient(135deg,#b23a2c,#e6e0da)" role="img" aria-label="Smartphone with a shopping cart button on screen"></div>
  <div class="tile abs" style="left:778px;top:2312px;background:linear-gradient(135deg,#c9d3dc,#3d4c63)" role="img" aria-label="Two engineers working at a server rack"></div>
</section>

<section class="band-grey abs" style="top:2740px;height:435px"></section>
<h2 class="section-title abs centered" style="top:2826px">Happy client says</h2>
<p class="quote-text abs" style="top:2906px">Lorem ipsum dolor sit amet, consectetuer adipiscing elit. Aenean commodo ligula eget dolor. Aenean massa. Cum sociis natoque penatibus et magnis dis parturient montes, nascetur ridiculus mus. Donec quam felis, ultricies nec, pellentesque eu, pretium quis, sem. Nulla consequat massa quis enim. Donec pede justo, fringilla vel, aliquet nec, vulputate eget, arcu. In enim justo, rhoncus ut.</p>
<p class="abs centered" style="top:3012px;font-size:15px">Daniel Corwin</p>
<p class="abs centered" style="top:3034px;font-size:10px;font-weight:700">CEO</p>
<div class="arrow-box light abs" style="left:86px;top:2935px"><svg width="12" height="18"><path d="M10 2L3 9l7 7" stroke="#555" stroke-width="2" fill="none"/></svg></div>
<div class="arrow-box light abs" style="left:1076px;top:2935px"><svg width="12" height="18"><path d="M2 2l7 7-7 7" stroke="#555" stroke-width="2" fill="none"/></svg></div>

<section class="blogs">
  <h2 class="section-title abs centered" style="top:3270px">Latest blogs</h2>
  <article class="blog-card abs" style="left:88px">
    <div class="thumb" style="background:linear-gradient(135deg,#2f5fb0,#d8e2f0)" role="img" aria-label="Close-up of a screen showing social media app icons"></div>
    <span class="tag">P4B</span>
    <h5>Plans4Buildables can help anyone turn their</h5>
    <small>Posted By Admin</small>
  </article>
  <article class="blog-card abs" style="left:436px">
    <div class="thumb" style="background:linear-gradient(180deg,#d8e6f4,#8fa9c4)" role="img" aria-label="Businessman looking up at city skyscrapers"></div>
    <span class="tag">P4B</span>
    <h5>Plans4Buildables can help anyone turn their</h5>
    <small>Posted By Admin</small>
  </article>
  <article class="blog-card abs" style="left:781px">
    <div class="thumb" style="background:linear-gradient(135deg,#2f5fb0,#d8e2f0)" role="img" aria-label="Close-up of a screen showing social media app icons"></div>
    <span class="tag">P4B</span>
    <h5>Plans4Buildables can help anyone turn their</h5>
    <small>Posted By Admin</small>
  </article>
  <div class="btn-navy abs" style="left:501px;top:3784px;width:198px;height:48px;font-size:15px">View All</div>
</section>

<footer class="site-footer abs">
  <h6 style="left:88px">About P4B</h6>
  <p class="about">Lorem ipsum dolor sit amet, consectetur adipisicing elit. Temporibus earum atque ide minus labore quaerat enim, velit magni quasi quibusdam. Explicabo vitae nemo modi praesentium, quos ab quisquam eius in incidunt.</p>
  <h6 style="left:467px">Get in touch</h6>
  <div class="contact-line" style="top:94px"><svg width="14" height="18" viewBox="0 0 14 18"><path d="M7 0a7 7 0 0 0-7 7c0 5 7 11 7 11s7-6 7-11a7 7 0 0 0-7-7z" fill="#fff"/><circle cx="7" cy="7" r="2.5" fill="#0f1e5a"/></svg>1250 Harbor View Rd, Lakeside, FL 33000</div>
  <div class="contact-line" style="top:134px"><svg width="16" height="16" viewBox="0 0 16 16"><path d="M3 1l3 3-2 2c1 2 3 4 6 6l2-2 3 3-2 2C7 15 1 9 1 3z" fill="#fff"/></svg>(555) 010-0199</div>
  <div class="contact-line" style="top:174px"><svg width="16" height="12" viewBox="0 0 16 12"><rect width="16" height="12" rx="1" fill="#fff"/><path d="M1 1l7 6 7-6" stroke="#0f1e5a" fill="none"/></svg>questions@plans4buildables-example.com</div>
  <h6 style="left:863px">Subscribe</h6>
  <p class="sub-copy">Temporibus earum atque ide minus labore quaerat enim, velit.</p>
  <div class="sub-field">Enter Your Email</div>
  <div class="sub-btn"><svg width="12" height="18"><path d="M2 2l7 7-7 7" stroke="#fff" stroke-width="2" fill="none"/></svg></div>
</footer>

<div class="bottom-bar abs">
  <p>© Copyrights P4B 2017. All rights reserved.</p>
  <span class="social" style="left:945px"></span>
  <span class="social" style="left:993px"></span>
  <span class="social" style="left:1041px"></span>
  <span class="social" style="left:1089px"></span>
</div>

</body>
</html>
```